Interior design service, along with home organization, packing, and staging, home and business. As well as staging in conjunction with real estate sales.
Updates

Love many of your designs and will be choosing today. To inform you of the exact details needed, the name of the company is "Touches by Marla T" , my phone number and e-,ail need to be included. i also need either description or some sort of bullet points that give an idea of the following:

- Interior design for home and business
- Home organization and packing
- Staging for personal and professional space
- Real estate stagingĀ 

Thank you

Target Market(s)

wide audience, but most importantly people looking for a quality service

Industry/Entity Type

Real Estate

Contact Information for Business Card

Touches By Marla T
Marla Tovendi
(555)614-2937
mtbrook@mailnest.example

Requirements
Must have
• I'm 29 so i want my card to reflect something professional but still fresh. I don't have any specific photos or quotes that Ive included, however I like the card to reflect a personal touch, which is what I'm seeking from this service in the design of my card. Thanks!

```html
<!DOCTYPE html>
<html lang="en">
<head>
<meta charset="utf-8">
<title>Touches By Marla T — Business Card</title>
<link rel="stylesheet" href="https://fonts.googleapis.com/css2?family=Tinos:wght@400;700&family=Tenor+Sans&display=swap">
<style>
  :root {
    --stage: #5a5a5c;
    --navy: #0f3763;
    --deep: #0a1f3f;
    --mid: #1768a8;
    --bright: #2fa0dc;
    --paper: #ffffff;
    --ink-light: #ffffff;
  }
  * { box-sizing: border-box; margin: 0; padding: 0; }
  html, body { width: 1200px; height: 960px; overflow: hidden; }
  body {
    background: var(--stage);
    display: flex;
    flex-direction: column;
    align-items: center;
    justify-content: center;
    gap: 40px;
    font-family: "Tinos", "Times New Roman", serif;
  }
  .card {
    position: relative;
    width: 700px;
    height: 400px;
    overflow: hidden;
    box-shadow: 0 8px 24px rgba(0,0,0,0.35);
  }
  .texture {
    position: absolute;
    left: 0; right: 0;
    background: linear-gradient(100deg, var(--deep) 0%, var(--mid) 55%, var(--bright) 100%);
  }

  /* Back: contact side */
  .card--back { background: var(--paper); }
  .card--back .texture--top { top: 0; height: 72px; }
  .card--back .texture--bottom { bottom: 0; height: 64px; }
  .tagline {
    position: absolute;
    top: 90px; left: 46px;
    font-size: 27px;
    font-weight: 700;
    color: var(--navy);
  }
  .services {
    position: absolute;
    top: 146px; left: 46px;
    width: 300px;
    list-style: none;
    color: var(--navy);
    font-size: 16px;
    line-height: 1.25;
  }
  .services li {
    position: relative;
    padding-left: 16px;
    margin-bottom: 9px;
  }
  .services li::before {
    content: "";
    position: absolute;
    left: 0; top: 7px;
    width: 6px; height: 6px;
    background: var(--navy);
  }
  .contact {
    position: absolute;
    top: 138px; right: 58px;
    text-align: right;
    color: var(--navy);
    font-weight: 700;
    padding-right: 22px;
    border-right: 9px solid var(--navy);
    line-height: 1.12;
  }
  .contact .label { font-size: 25px; }
  .contact .value { font-size: 18px; margin-bottom: 6px; }
  .contact .value:last-child { margin-bottom: 0; }

  /* Front: message side */
  .card--front .texture--full { top: 0; bottom: 0; }
  .headline {
    position: absolute;
    top: 72px; left: 44px;
    color: var(--ink-light);
    font-family: "Tenor Sans", "Optima", sans-serif;
    font-weight: 400;
    line-height: 1.1;
  }
  .headline .lead { display: block; font-size: 34px; }
  .headline .emphasis { display: block; font-size: 46px; margin-left: 150px; }
  .name-band {
    position: absolute;
    left: 0; right: 0;
    top: 284px; height: 62px;
    background: var(--paper);
    padding: 8px 0 0 40px;
    color: var(--navy);
    font-weight: 700;
  }
  .name-band .intro { display: block; font-size: 13px; line-height: 1; }
  .name-band .owner { display: block; font-size: 30px; line-height: 1.15; }
</style>
</head>
<body>
  <section class="card card--back" aria-label="Business card, contact side">
    <div class="texture texture--top" role="img" aria-label="Blue paint-splatter texture band"></div>
    <h2 class="tagline">Interior design service to home and business</h2>
    <ul class="services">
      <li>Interior design for home and business</li>
      <li>Home organization and packing</li>
      <li>Staging for personal and professional space</li>
      <li>Real estate staging</li>
    </ul>
    <div class="contact">
      <div class="label">NAME</div>
      <div class="value">MARLA TOVENDI</div>
      <div class="label">Phone</div>
      <div class="value">(555)614-2937</div>
      <div class="label">Email</div>
      <div class="value">mtbrook@mailnest.example</div>
    </div>
    <div class="texture texture--bottom" role="img" aria-label="Blue paint-splatter texture band"></div>
  </section>

  <section class="card card--front" aria-label="Business card, message side">
    <div class="texture texture--full" role="img" aria-label="Blue paint-splatter texture background"></div>
    <h1 class="headline">
      <span class="lead">Are you looking for a</span>
      <span class="emphasis">quality service?</span>
    </h1>
    <div class="name-band">
      <span class="intro">Touches By,</span>
      <span class="owner">Marla T — Marla Tovendi</span>
    </div>
  </section>
</body>
</html>
```